Business card design for Automotive workshop

We need a business card for a new automotive repair and tyre shop called Ridgeback Prime Automotive located in New Zealand. We are a clean, modern and fresh workshop and company.

Front needs to feature logo,
my name:
Lachie Westergaard (director)

Address:
48 Marlow Lane
Pohutu Bay 3582

Phone: 07 842 1937
Mobile: 027 519 2764
Email: office@ridgebackmotors.co.nz
Website: ridgebackmotors.co.nz

Back needs to feature an area to write down appointment details, date and time.

Also feature a list of jobs and work we do such as,
Vehicle Servicing
All Mechanical Repairs
Warrant of Fitness
Tyres & Wheel Alignments
Automotive Diagnostics
Automotive Parts & Supplies

```html
<!DOCTYPE html>
<html lang="en">
<head>
<meta charset="utf-8">
<title>Ridgeback Prime Automotive – Business Card</title>
<link rel="stylesheet" href="https://fonts.googleapis.com/css2?family=Open+Sans:wght@400;600;700&family=PT+Sans+Narrow:wght@700&display=swap">
<style>
  :root {
    --stage: #d6d8d7;
    --card: #222222;
    --red: #e31e2a;
    --white: #ffffff;
    --soft: #e6e6e6;
    --rule: #3c3c3c;
    --ink: #333333;
  }
  * { box-sizing: border-box; margin: 0; padding: 0; }
  html, body { width: 1200px; height: 900px; overflow: hidden; }
  body {
    background: var(--stage);
    font-family: "Open Sans", Arial, sans-serif;
    display: flex;
    flex-direction: column;
    align-items: center;
    justify-content: center;
    gap: 40px;
  }
  .card {
    position: relative;
    width: 620px;
    height: 378px;
    background: var(--card);
    color: var(--soft);
    overflow: hidden;
  }

  /* brand name block */
  .brand {
    display: flex;
    align-items: center;
    gap: 12px;
    color: var(--red);
    font-weight: 700;
    text-transform: uppercase;
    line-height: 1.05;
    white-space: nowrap;
  }
  .brand-mark {
    width: 18px;
    height: 18px;
    background: var(--red);
    flex: none;
  }

  /* back side */
  .card-back .brand {
    position: absolute;
    left: 44px;
    top: 38px;
    font-size: 30px;
    letter-spacing: 1px;
  }
  .services {
    position: absolute;
    left: 58px;
    top: 120px;
    display: grid;
    grid-template-columns: 250px 250px;
    row-gap: 4px;
    list-style: none;
    font-size: 15px;
  }
  .services li::before {
    content: "•";
    color: var(--red);
    margin-right: 6px;
  }
  .appointment-title {
    position: absolute;
    left: 0;
    right: 0;
    top: 206px;
    text-align: center;
    color: var(--red);
    font-weight: 700;
    font-size: 19px;
    letter-spacing: 0.5px;
  }
  .appointment-strip {
    position: absolute;
    left: 14px;
    right: 14px;
    bottom: 22px;
    height: 100px;
    background: var(--white);
    display: flex;
    align-items: flex-end;
    gap: 30px;
    padding: 0 30px 26px;
    color: var(--ink);
    font-size: 15px;
  }
  .field { display: flex; align-items: flex-end; gap: 8px; }
  .field-date { flex: 1.7; }
  .field-time { flex: 1; }
  .field-line { flex: 1; border-bottom: 1px solid var(--ink); height: 1px; margin-bottom: 4px; }

  /* front side */
  .card-front .brand {
    position: absolute;
    left: 40px;
    top: 178px;
    font-size: 22px;
    letter-spacing: 1px;
  }
  .divider {
    position: absolute;
    left: 318px;
    top: 60px;
    width: 1px;
    height: 170px;
    background: var(--rule);
  }
  .contact {
    position: absolute;
    left: 340px;
    top: 60px;
  }
  .contact-name {
    font-family: "PT Sans Narrow", "Arial Narrow", sans-serif;
    font-weight: 700;
    color: var(--red);
    font-size: 27px;
    line-height: 1.05;
  }
  .contact-role { font-size: 14px; margin-bottom: 10px; }
  .contact-address { font-size: 14px; margin-bottom: 4px; }
  .contact-list { list-style: none; font-size: 14px; line-height: 1.55; }
  .contact-list li { display: flex; align-items: center; gap: 8px; }
  .contact-list svg { width: 13px; height: 13px; flex: none; }
</style>
</head>
<body>

  <section class="card card-back" aria-label="Card back">
    <div class="brand"><span class="brand-mark"></span><span>Ridgeback Prime<br>Automotive</span></div>
    <ul class="services">
      <li>Vehicle Servicing</li>
      <li>Tyres &amp; Wheel Alignments</li>
      <li>All Mechanical Repairs</li>
      <li>Automotive Diagnostics</li>
      <li>Automotive Parts &amp; Supplies</li>
      <li>Warrant of Fitness</li>
    </ul>
    <h2 class="appointment-title">APPOINTMENT</h2>
    <div class="appointment-strip">
      <div class="field field-date"><span>Date</span><span class="field-line"></span></div>
      <div class="field field-time"><span>Time</span><span class="field-line"></span></div>
    </div>
  </section>

  <section class="card card-front" aria-label="Card front">
    <div class="brand"><span class="brand-mark"></span><span>Ridgeback Prime<br>Automotive</span></div>
    <div class="divider"></div>
    <div class="contact">
      <p class="contact-name">Lachie Westergaard</p>
      <p class="contact-role">Director</p>
      <p class="contact-address">48 Marlow Lane, Pohutu Bay 3582</p>
      <ul class="contact-list">
        <li>
          <svg viewBox="0 0 16 16" aria-hidden="true"><path fill="#e31e2a" d="M3.5 1l3 3-1.6 1.8a9 9 0 0 0 5.3 5.3L12 9.5l3 3-2 2.2C7.5 14.5 1.5 8.5 1.3 3z"/></svg>
          <span>07 842 1937</span>
        </li>
        <li>
          <svg viewBox="0 0 16 16" aria-hidden="true"><rect x="4" y="1" width="8" height="14" rx="1.5" fill="none" stroke="#e31e2a" stroke-width="1.6"/><circle cx="8" cy="12.5" r="0.9" fill="#e31e2a"/></svg>
          <span>027 519 2764</span>
        </li>
        <li>
          <svg viewBox="0 0 16 16" aria-hidden="true"><rect x="1" y="3" width="14" height="10" fill="none" stroke="#e31e2a" stroke-width="1.6"/><path d="M1 3l7 6 7-6" fill="none" stroke="#e31e2a" stroke-width="1.6"/></svg>
          <span>office@ridgebackmotors.co.nz</span>
        </li>
        <li>
          <svg viewBox="0 0 16 16" aria-hidden="true"><circle cx="8" cy="8" r="6.5" fill="none" stroke="#e31e2a" stroke-width="1.4"/><ellipse cx="8" cy="8" rx="2.8" ry="6.5" fill="none" stroke="#e31e2a" stroke-width="1.2"/><path d="M1.5 8h13" stroke="#e31e2a" stroke-width="1.2"/></svg>
          <span>ridgebackmotors.co.nz</span>
        </li>
      </ul>
    </div>
  </section>

</body>
</html>
```